Moderne Visitenkarten für Medizintechnikfirma
Zielgruppe
Vertriebsfirma von moderner und innovativer Medizintechnik
Zielgruppe: Ärzte, Kliniken, Medizintechnikfirmen, Patienten
Aufgabenstellung
Besonderes, modernes, auffälliges und ansprechendes Design ohne überladen oder aufdringlich zu sein
Farbenorientierung kann am Logo und der Website geschehen. Wenn zum Logo harmonierend, sind aber auch andere Farben gerne gesehen.
Format: eher horizontal, vertikal aber auch möglich, abgerundete Ecken einplanen
Wenn möglich folgende Infos bitte schon auf die Karten bringen (pro Person eine Karte):
Harald Zumbrink (CEO)
harald.zumbrink@vitalnova-partner.de
(VitalNova Partner GmbH
Lärchenstraße 14
49377 Fallrode)
www.vitalnova-partner.de
info@vitalnova-partner.de
Jannik Sprau (CoS)
jannik.sprau@vitalnova-partner.de
Die allgemeinen Firmeninfos können deutlich kleiner sein. Anschrift nur wenn es dadurch nicht zu viel werden würde.

```html
<!DOCTYPE html>
<html lang="de">
<head>
<meta charset="utf-8">
<title>VitalNova Partner – Visitenkarten</title>
<link rel="stylesheet" href="https://fonts.googleapis.com/css2?family=Arimo:wght@400;700&display=swap">
<style>
  :root {
    --bg: #ecebe8;
    --card: #ffffff;
    --accent: #e2401e;
    --brand: #4b3f8e;
    --ink: #2c2c34;
    --muted: #5a5a66;
    --shadow: rgba(0, 0, 0, 0.14);
  }
  * { box-sizing: border-box; margin: 0; padding: 0; }
  html, body {
    width: 1200px; height: 912px; overflow: hidden;
    background: var(--bg);
    font-family: "Arimo", Arial, sans-serif;
    color: var(--ink);
  }
  .sheet {
    width: 1200px; height: 912px;
    display: flex; flex-direction: column;
    align-items: center; justify-content: center; gap: 64px;
  }
  .card {
    position: relative;
    width: 600px; height: 350px;
    background: var(--card);
    border-radius: 14px;
    box-shadow: 0 10px 28px var(--shadow);
    overflow: hidden;
  }

  /* Front: personal details */
  .brand-mark {
    position: absolute; top: 34px; right: 40px;
    display: flex; align-items: center; gap: 10px;
  }
  .brand-mark .dot {
    width: 14px; height: 14px; border-radius: 50%;
    background: var(--brand);
  }
  .brand-mark .name {
    font-size: 24px; font-weight: 400; color: var(--brand);
  }
  .rule-top {
    position: absolute; top: 96px; left: 262px; right: 40px;
    height: 2px; background: var(--accent);
  }
  .company {
    position: absolute; top: 114px; left: 392px;
    font-size: 13.5px; line-height: 1.38; color: var(--muted);
  }
  .company .web { color: var(--accent); }
  .person {
    position: absolute; left: 40px; top: 190px;
  }
  .person .full-name {
    font-size: 25px; font-weight: 700; color: var(--accent);
  }
  .person .role {
    font-size: 10px; color: var(--muted); margin-top: 2px; letter-spacing: 0.05em;
  }
  .rule-name {
    position: absolute; left: 40px; top: 252px; width: 290px;
    height: 2px; background: var(--accent);
  }
  .contact {
    position: absolute; left: 40px; top: 268px;
    list-style: none; font-size: 14px; color: var(--ink);
  }
  .contact li { display: flex; align-items: center; gap: 12px; height: 26px; }
  .contact .icon {
    width: 16px; height: 16px; border-radius: 3px;
    background: var(--accent);
    display: flex; align-items: center; justify-content: center;
  }
  .contact .email { font-size: 12.5px; }

  /* Back: brand side */
  .card-back { display: flex; align-items: center; justify-content: center; }
  .card-back::after {
    content: ""; position: absolute; left: 0; right: 0; bottom: 0;
    height: 8px; background: var(--brand);
  }
  .card-back .brand-mark { position: static; gap: 16px; }
  .card-back .brand-mark .dot { width: 26px; height: 26px; }
  .card-back .brand-mark .name { font-size: 40px; }
</style>
</head>
<body>
<main class="sheet">

  <section class="card card-front" aria-label="Visitenkarte Vorderseite">
    <div class="brand-mark">
      <span class="dot"></span>
      <span class="name">VitalNova Partner</span>
    </div>
    <div class="rule-top"></div>

    <address class="company" style="font-style:normal">
      (VitalNova Partner GmbH<br>
      Lärchenstraße 14<br>
      49377 Fallrode)<br>
      <span class="web">www.vitalnova-partner.de</span><br>
      info@vitalnova-partner.de<br>
      0800-5309186
    </address>

    <div class="person">
      <h1 class="full-name">Harald Zumbrink</h1>
      <p class="role">CEO</p>
    </div>
    <div class="rule-name"></div>

    <ul class="contact">
      <li>
        <span class="icon">
          <svg width="10" height="12" viewBox="0 0 10 12" aria-hidden="true">
            <rect x="1.5" y="0.8" width="7" height="10.4" rx="1.2" fill="none" stroke="#fff" stroke-width="1.3"/>
            <circle cx="5" cy="9.2" r="0.8" fill="#fff"/>
          </svg>
        </span>
        +4915290417736
      </li>
      <li>
        <span class="icon">
          <svg width="12" height="10" viewBox="0 0 12 10" aria-hidden="true">
            <rect x="0.8" y="1" width="10.4" height="8" rx="1" fill="none" stroke="#fff" stroke-width="1.2"/>
            <path d="M1 1.5 L6 5.5 L11 1.5" fill="none" stroke="#fff" stroke-width="1.2"/>
          </svg>
        </span>
        <span class="email">harald.zumbrink@vitalnova-partner.de</span>
      </li>
    </ul>
  </section>

  <section class="card card-back" aria-label="Visitenkarte Rückseite">
    <div class="brand-mark">
      <span class="dot"></span>
      <span class="name">VitalNova Partner</span>
    </div>
  </section>

</main>
</body>
</html>
```